Mental Health care Company in Washington DC

We are a new mental health care services provider in Washington DC. Please look at these sites.
https://quarrystonewellbeingpartners.com
https://www.quietharborllc.com
https://fernvale-nb.org/
https://www.truepathnb.com
https://www.willowmeadnb.com

```html
<!DOCTYPE html>
<html lang="en">
<head>
<meta charset="utf-8">
<title>Lumen Harbor Wellness – Mental Health Care in Washington, DC</title>
<link rel="stylesheet" href="https://fonts.googleapis.com/css2?family=Mulish:wght@400;500;600;700&family=Roboto+Condensed:wght@700&family=Arimo:wght@400&display=swap">
<style>
:root{
  --navy:#0f2650;
  --ink:#1d2233;
  --teal:#a8dbd8;
  --teal-soft:#f2f9f9;
  --cream:#fcf8f4;
  --orange:#f2a463;
  --rule:#b9bcc4;
  --white:#ffffff;
}
*{box-sizing:border-box;margin:0;padding:0}
html,body{width:1200px;height:3670px;overflow:hidden;background:var(--white)}
body{font-family:"Mulish",sans-serif;color:var(--navy)}
.page{position:relative;width:1200px;height:3670px;overflow:hidden}
.band{position:absolute;left:0;width:1200px}
.abs{position:absolute}
.body-copy{font-family:"Arimo",sans-serif;font-size:12px;line-height:23px;color:var(--ink)}
.btn{position:absolute;display:flex;align-items:center;justify-content:center;border-radius:22px;background:var(--teal);color:var(--navy);font-size:15px;font-weight:600}
.rule{height:2px;width:50px;background:var(--rule)}

/* brand */
.brand{position:absolute;color:var(--navy);font-weight:600;line-height:1}
.brand .name{font-size:38px;letter-spacing:-0.5px}
.brand .tag{display:flex;align-items:center;gap:8px;font-size:14px;letter-spacing:8px;margin-top:4px}
.brand .tag::before,.brand .tag::after{content:"";width:30px;height:1px;background:var(--navy)}

/* header */
.site-header{top:0;height:88px;background:var(--white)}
.topline{position:absolute;left:527px;width:530px;top:40px;height:1px;background:#e3e5ea}
.call-strip{position:absolute;left:645px;top:13px;font-size:12px;font-weight:500;display:flex;align-items:center;gap:10px}
.call-strip .num{color:var(--orange);display:flex;align-items:center;gap:5px;font-size:13px}
.social{display:flex;gap:8px}
.social span{width:22px;height:22px;border-radius:50%;background:var(--teal);display:block}
.nav{position:absolute;top:62px;left:0;width:1200px;font-size:13px;font-weight:600}
.nav a{position:absolute;color:var(--navy);text-decoration:none}

/* hero */
.hero{top:88px;height:494px;background:linear-gradient(100deg,#b79a7a 0%,#caa478 35%,#e7c08a 55%,#8a6a4b 80%,#5d4a3b 100%)}
.hero-title{position:absolute;left:142px;top:122px;font-family:"Roboto Condensed",sans-serif;font-weight:700;font-size:58px;line-height:61px;color:var(--navy)}
.hero .btn{left:141px;top:258px;width:127px;height:40px;background:var(--white);color:var(--navy)}
.hero-info{position:absolute;left:152px;top:314px;color:var(--white);font-size:12px;font-weight:500}
.hero-phone{position:absolute;left:150px;top:336px;color:var(--white);font-size:21px;display:flex;align-items:center;gap:8px}

/* welcome */
.welcome{top:582px;height:554px}
.photo{position:absolute}
.welcome .photo{left:140px;top:81px;width:411px;height:383px;background:linear-gradient(135deg,#e8ecef,#c9d6e0 45%,#9fb7cb 70%,#dfe3e6)}
.welcome-text{position:absolute;left:598px;top:70px;width:470px}
.eyebrow{font-size:24px;font-weight:500;line-height:28px}
.big-title{font-size:38px;font-weight:600;line-height:44px}
.subhead{font-size:16px;font-weight:600;margin:20px 0 8px}
.welcome .btn{left:598px;top:434px;width:127px;height:41px}

/* services */
.services{top:1136px;height:757px;background:var(--cream)}
.section-head{position:absolute;left:0;width:1200px;text-align:center}
.section-head .eyebrow{font-size:24px}
.section-head .rule{margin:6px auto 0}
.petal{position:absolute}
.petal.top{left:554px;top:188px;width:92px;height:161px;border-radius:46px 46px 0 0;background:linear-gradient(180deg,#c9d8d6,#b08d70)}
.petal.left{left:392px;top:349px;width:162px;height:91px;border-radius:46px 0 0 46px;background:linear-gradient(90deg,#c9a182,#e3c4a8)}
.petal.right{left:646px;top:349px;width:162px;height:91px;border-radius:0 46px 46px 0;background:linear-gradient(90deg,#d3e4e4,#8fb8bb)}
.petal.bottom{left:554px;top:440px;width:92px;height:162px;border-radius:0 0 46px 46px;background:linear-gradient(180deg,#d9cfc6,#a7785b)}
.icon-dot{position:absolute;width:62px;height:62px;border-radius:50%;background:var(--white);box-shadow:0 4px 12px rgba(15,38,80,.12);display:flex;align-items:center;justify-content:center}
.service{position:absolute;width:300px}
.service h3{font-size:13px;font-weight:700;margin-bottom:6px}
.service p{font-family:"Arimo",sans-serif;font-size:12px;line-height:20px;color:var(--ink)}
.service.l{text-align:right}
.services .btn{left:551px;top:637px;width:127px;height:41px}

/* first step */
.first-step{top:1893px;height:537px}
.first-step .text{position:absolute;left:141px;top:128px;width:405px}
.first-step h2{font-size:32px;font-weight:600;margin-bottom:10px}
.contact-list{list-style:none;margin-top:12px}
.contact-list li{display:flex;align-items:center;gap:14px;font-size:13px;font-weight:600;height:33px}
.first-step .btn{left:141px;top:360px;width:175px;height:41px}
.first-step .photo{left:613px;top:78px;width:446px;height:383px;background:linear-gradient(120deg,#d8e0e4,#b5c5ce 40%,#e8e3dc 70%,#c9c2b6)}

/* community */
.community{top:2430px;height:392px;background:var(--teal-soft)}
.community .illus{position:absolute;left:60px;top:78px;width:530px;height:242px;border-radius:12px;background:radial-gradient(circle at 50% 40%,#f3b26b 0,#4f8fa0 25%,#cfe7e6 55%,var(--teal-soft) 80%)}
.community .text{position:absolute;left:613px;top:80px;width:440px}
.community .text p{margin-top:18px;padding-left:4px}
.community .btn{left:613px;top:272px;width:175px;height:41px}

/* contact */
.contact{top:2822px;height:698px}
.contact .section-head .big-title{font-size:38px}
.contact .intro{position:absolute;left:160px;width:880px;top:160px;text-align:center}
.contact-box{position:absolute;left:182px;top:228px;width:834px;height:444px;display:flex;border:1px solid #eadccd}
.contact-box .details{width:416px;background:var(--cream);padding:60px 0 0 36px;position:relative}
.contact-box .inquiry{flex:1;background:var(--teal-soft);border-left:1px solid #cfe3e6;padding:60px 0 0 38px;position:relative}
.box-title{font-size:21px;font-weight:600}
.box-title + .rule{margin-top:14px}
.details .note{font-size:11px;line-height:22px;color:var(--ink);margin-top:18px;width:330px}
.detail-row{display:flex;align-items:center;gap:16px;font-size:13px;color:var(--ink);margin-top:12px;line-height:20px}
.detail-row .dot{width:36px;height:36px;border-radius:50%;background:var(--orange);display:flex;align-items:center;justify-content:center;flex:none}
.follow{display:flex;align-items:center;gap:8px;font-size:16px;font-weight:600;margin-top:22px}
.follow span{width:27px;height:27px;border-radius:50%;background:var(--navy);display:block}
.field{position:absolute;left:38px;width:340px;border-bottom:1px solid var(--rule);font-size:12px;color:var(--ink);display:flex;align-items:flex-start;gap:10px;padding-bottom:8px}
.inquiry .btn{left:47px;top:343px;width:98px;height:40px}

/* footer */
.site-footer{top:3520px;height:107px}
.site-footer .nav{top:50px}
.copyright{top:3627px;height:43px;background:var(--orange);display:flex;align-items:center;justify-content:center;font-size:13px;color:var(--navy);font-weight:500}
</style>
</head>
<body>
<div class="page">

  <header class="band site-header">
    <div class="brand" style="left:142px;top:14px"><div class="name">Lumen Harbor</div><div class="tag">WELLNESS</div></div>
    <div class="call-strip">For More Information Call Us Today
      <span class="num"><svg width="14" height="14" viewBox="0 0 24 24" fill="none" stroke="#f2a463" stroke-width="2"><path d="M5 3h4l2 5-3 2a11 11 0 0 0 6 6l2-3 5 2v4a2 2 0 0 1-2 2A18 18 0 0 1 3 5a2 2 0 0 1 2-2z"/></svg>555.014.2280</span>
      <span class="social"><span></span><span></span></span>
    </div>
    <div class="topline"></div>
    <nav class="nav">
      <a style="left:523px">Home</a><a style="left:598px">About Us</a><a style="left:697px">Services We Provide</a><a style="left:866px">Employment</a><a style="left:985px">Contact Us</a>
    </nav>
  </header>

  <section class="band hero" role="img" aria-label="Photo of a person in a hat holding a smiling yellow ball against a sunset over hills">
    <h1 class="hero-title">Your Mental Wellness.<br>Our National Priority</h1>
    <div class="btn">Know More</div>
    <div class="hero-info">For More Information Call Us Today</div>
    <div class="hero-phone"><svg width="22" height="22" viewBox="0 0 24 24" fill="none" stroke="#fff" stroke-width="1.6"><path d="M5 3h4l2 5-3 2a11 11 0 0 0 6 6l2-3 5 2v4a2 2 0 0 1-2 2A18 18 0 0 1 3 5a2 2 0 0 1 2-2z"/></svg>555.014.2280</div>
  </section>

  <section class="band welcome">
    <div class="photo" role="img" aria-label="Photo of a therapist taking notes while a man listens in a bright office"></div>
    <div class="welcome-text">
      <div class="eyebrow">Welcome to</div>
      <h2 class="big-title">Lumen Harbor Wellness</h2>
      <div class="rule" style="margin-top:8px"></div>
      <h3 class="subhead">Compassionate Mental Health Care in Washington, DC</h3>
      <p class="body-copy">At Lumen Harbor Wellness, we believe that mental wellness is essential to living a full and meaningful life. Located in the heart of Washington, DC, our practice is committed to supporting individuals, couples, and families on their journey to emotional well-being.</p>
      <h3 class="subhead" style="margin-top:16px">Your Partner in Healing &amp; Growth</h3>
      <p class="body-copy">Whether you're navigating anxiety, depression, trauma, relationship challenges, or simply looking for support in life transitions, our team of licensed mental health professionals is here to help. We provide a safe, inclusive, and confidential space where you can feel heard, respected, and empowered to heal</p>
    </div>
    <div class="btn">Know More</div>
  </section>

  <section class="band services">
    <div class="section-head" style="top:76px">
      <div class="eyebrow">Our Specialties</div>
      <h2 class="big-title">Services We Provide</h2>
      <div class="rule"></div>
    </div>
    <div class="petal top" role="img" aria-label="Photo of a smiling woman with curly hair"></div>
    <div class="petal left" role="img" aria-label="Photo of a counselling session in warm light"></div>
    <div class="petal right" role="img" aria-label="Photo of a calm therapy room"></div>
    <div class="petal bottom" role="img" aria-label="Photo of hands in a supportive conversation"></div>

    <div class="icon-dot" style="left:475px;top:225px"><svg width="32" height="32" viewBox="0 0 32 32" fill="none" stroke="#0f2650" stroke-width="1.5"><circle cx="9" cy="10" r="3"/><circle cx="23" cy="10" r="3"/><path d="M5 26v-8h8v8M19 26v-8h8v8"/><circle cx="16" cy="5" r="3" stroke="#f2a463"/></svg></div>
    <div class="icon-dot" style="left:676px;top:225px"><svg width="32" height="32" viewBox="0 0 32 32" fill="none" stroke="#0f2650" stroke-width="1.5"><circle cx="8" cy="12" r="3"/><circle cx="24" cy="12" r="3"/><path d="M3 26v-7h10v7M19 26v-7h10v7M12 21h8"/><circle cx="17" cy="5" r="3" stroke="#f2a463"/></svg></div>
    <div class="icon-dot" style="left:475px;top:482px"><svg width="32" height="32" viewBox="0 0 32 32" fill="none" stroke="#0f2650" stroke-width="1.5"><path d="M10 28v-6a9 9 0 1 1 12-4l2 4h-3v6"/><circle cx="16" cy="12" r="4" stroke="#f2a463"/></svg></div>
    <div class="icon-dot" style="left:676px;top:482px"><svg width="32" height="32" viewBox="0 0 32 32" fill="none" stroke="#0f2650" stroke-width="1.5"><path d="M4 16l5 10M28 16l-5 10M9 20l4 4M23 20l-4 4"/><circle cx="12" cy="8" r="3" stroke="#f2a463"/><circle cx="20" cy="8" r="3" stroke="#f2a463"/></svg></div>

    <div class="service l" style="left:149px;top:224px"><h3>Individual Therapy</h3><p>Ut wisi enim ad minim veniam, quis nostrud exerci tation ullamcorper suscipit lobortis nisl ut aliquip ex ea commodo consequat.</p></div>
    <div class="service" style="left:754px;top:218px"><h3>Couples &amp; Family Counseling</h3><p>Ut wisi enim ad minim veniam, quis nostrud exerci tation ullamcorper suscipit lobortis nisl ut aliquip ex ea commodo consequat.</p></div>
    <div class="service l" style="left:149px;top:469px"><h3>Psychiarty</h3><p>Ut wisi enim ad minim veniam, quis nostrud exerci tation ullamcorper suscipit lobortis nisl ut aliquip ex ea commodo consequat.</p></div>
    <div class="service" style="left:754px;top:469px"><h3>Community Support Services</h3><p>Ut wisi enim ad minim veniam, quis nostrud exerci tation ullamcorper suscipit lobortis nisl ut aliquip ex ea commodo consequat.</p></div>
    <div class="btn">Know More</div>
  </section>

  <section class="band first-step">
    <div class="text">
      <h2>Take the First Step Today</h2>
      <p class="body-copy">Seeking support is a sign of strength. If you're ready to begin your journey toward healing, we're here to walk with you every step of the way.</p>
      <ul class="contact-list">
        <li><svg width="18" height="18" viewBox="0 0 24 24" fill="none" stroke="#f2a463" stroke-width="1.6"><path d="M5 3h4l2 5-3 2a11 11 0 0 0 6 6l2-3 5 2v4a2 2 0 0 1-2 2A18 18 0 0 1 3 5a2 2 0 0 1 2-2z"/></svg>Call us at 555.014.2280</li>
        <li><svg width="18" height="18" viewBox="0 0 24 24" fill="none" stroke="#f2a463" stroke-width="1.6"><path d="M12 22s7-7 7-12a7 7 0 0 0-14 0c0 5 7 12 7 12z"/><circle cx="12" cy="10" r="2.5"/></svg>Visit us at : Street Name, City Name, State Zipcode</li>
        <li><svg width="18" height="18" viewBox="0 0 24 24" fill="none" stroke="#f2a463" stroke-width="1.6"><rect x="3" y="5" width="16" height="15" rx="1"/><path d="M3 10h16M8 3v4M14 3v4"/></svg>Schedule an appointment online</li>
      </ul>
    </div>
    <div class="btn">Contact Us Today</div>
    <div class="photo" role="img" aria-label="Photo of a counsellor with a clipboard talking with a young woman on a sofa"></div>
  </section>

  <section class="band community">
    <div class="illus" role="img" aria-label="Illustration of health workers assembling a colourful puzzle heart among leafy branches"></div>
    <div class="text">
      <h2 class="big-title" style="line-height:40px">Rooted in Community,<br>Guided by Care</h2>
      <p class="body-copy">As part of the vibrant and diverse DC community, we honor the unique experiences of every individual we serve. Our team brings cultural competence, evidence-based practices, and a deep commitment to mental health equity.</p>
    </div>
    <div class="btn">Contact Us Today</div>
  </section>

  <section class="band contact">
    <div class="section-head" style="top:74px">
      <h2 class="big-title">Contact Us</h2>
      <div class="rule" style="margin-top:10px"></div>
    </div>
    <p class="intro body-copy">Have questions or need help getting started? Our team is here to support you. Reach out today — whether you're looking to schedule an appointment, learn more about our services, or simply talk to someone who cares.</p>
    <div class="contact-box">
      <div class="details">
        <div class="box-title">Contact Details</div>
        <div class="rule"></div>
        <p class="note">Every message is confidential, and we're committed to responding promptly.</p>
        <div class="detail-row" style="margin-top:18px"><span class="dot"><svg width="18" height="18" viewBox="0 0 24 24" fill="none" stroke="#0f2650" stroke-width="1.8"><path d="M12 22s7-7 7-12a7 7 0 0 0-14 0c0 5 7 12 7 12z"/><circle cx="12" cy="10" r="2.5"/></svg></span><span>Street Name, City Name<br>State Zipcode</span></div>
        <div class="detail-row"><span class="dot"><svg width="18" height="18" viewBox="0 0 24 24" fill="none" stroke="#0f2650" stroke-width="1.8"><rect x="3" y="6" width="18" height="13" rx="1"/><path d="M3 7l9 7 9-7"/></svg></span><span>hello@lumenharbor.example</span></div>
        <div class="detail-row"><span class="dot"><svg width="18" height="18" viewBox="0 0 24 24" fill="none" stroke="#0f2650" stroke-width="1.8"><path d="M5 3h4l2 5-3 2a11 11 0 0 0 6 6l2-3 5 2v4a2 2 0 0 1-2 2A18 18 0 0 1 3 5a2 2 0 0 1 2-2z"/></svg></span><span>555–014–2280</span></div>
        <div class="follow">Follow Us: <span></span><span></span></div>
      </div>
      <div class="inquiry">
        <div class="box-title">Quick Inquiry</div>
        <div class="rule"></div>
        <div class="field" style="top:125px"><svg width="14" height="14" viewBox="0 0 24 24" fill="none" stroke="#f2a463" stroke-width="1.8"><circle cx="12" cy="8" r="4"/><path d="M4 21a8 8 0 0 1 16 0"/></svg>Name</div>
        <div class="field" style="top:173px"><svg width="14" height="14" viewBox="0 0 24 24" fill="none" stroke="#f2a463" stroke-width="1.8"><rect x="3" y="6" width="18" height="13" rx="1"/><path d="M3 7l9 7 9-7"/></svg>Email</div>
        <div class="field" style="top:223px"><svg width="14" height="14" viewBox="0 0 24 24" fill="none" stroke="#f2a463" stroke-width="1.8"><path d="M5 3h4l2 5-3 2a11 11 0 0 0 6 6l2-3 5 2v4a2 2 0 0 1-2 2A18 18 0 0 1 3 5a2 2 0 0 1 2-2z"/></svg>Phone</div>
        <div class="field" style="top:273px;height:55px"><svg width="14" height="14" viewBox="0 0 24 24" fill="none" stroke="#f2a463" stroke-width="1.8"><path d="M4 4h16v12H9l-5 4z"/></svg>Message</div>
        <div class="btn">Submit</div>
      </div>
    </div>
  </section>

  <footer class="band site-footer">
    <div class="brand" style="left:140px;top:28px"><div class="name">Lumen Harbor</div><div class="tag">WELLNESS</div></div>
    <nav class="nav">
      <a style="left:523px">Home</a><a style="left:598px">About Us</a><a style="left:697px">Services We Provide</a><a style="left:866px">Employment</a><a style="left:985px">Contact Us</a>
    </nav>
  </footer>
  <div class="band copyright">© 2025. Lumen Harbor Wellness.&nbsp; All Rights Reserved.</div>

</div>
</body>
</html>
```